Stationery Design Project

We need, stationary designs for a store of children and juvenile furniture.
we have the logo. also need tags for the furniture with enought space to include description and options , maybe a 4" x 6" tag.

Target Market(s)

Parents of childrens and teens

Industry/Entity Type

Store

```html
<!DOCTYPE html>
<html lang="en">
<head>
<meta charset="utf-8">
<title>Nestling Rooms Stationery</title>
<link href="https://fonts.googleapis.com/css2?family=Open+Sans:wght@400;600;700&family=Arimo:wght@400&display=swap" rel="stylesheet">
<style>
  :root {
    --teal: #55c4d1;
    --orange: #f2711c;
    --ink: #2b2b2b;
    --grey: #6b6b6b;
    --brand-grey: #5a5a5a;
    --cloud: #e3e3e3;
    --paper: #ffffff;
    --backdrop: #ebebeb;
  }
  * { margin: 0; padding: 0; box-sizing: border-box; }
  html, body { width: 1200px; height: 900px; overflow: hidden; }
  body {
    position: relative;
    background: radial-gradient(ellipse at 50% 45%, #f7f7f7 0%, var(--backdrop) 75%);
    font-family: "Open Sans", sans-serif;
    color: var(--ink);
  }

  /* Business card – front */
  .card {
    position: absolute;
    left: 125px;
    width: 332px;
    height: 192px;
    border-radius: 16px;
  }
  .card-front { top: 245px; background: var(--paper); }
  .card-back  { top: 478px; background: var(--teal); }

  .brand {
    position: absolute;
    font-weight: 600;
    color: var(--brand-grey);
    white-space: nowrap;
  }
  .card-front .brand { right: 16px; top: 38px; font-size: 16px; display: flex; align-items: center; gap: 6px; }
  .brand-square { width: 12px; height: 12px; background: var(--teal); display: inline-block; }

  .cloud-decor {
    position: absolute;
    background: var(--cloud);
    border-radius: 18px;
    opacity: .8;
  }
  .card-front .cloud-decor { left: 18px; top: 50px; width: 110px; height: 38px; }

  .holder-name { position: absolute; left: 16px; top: 98px; font-size: 16px; font-weight: 600; color: var(--orange); }
  .holder-role { position: absolute; left: 16px; top: 116px; font-size: 10px; color: var(--grey); }
  .contact-row { position: absolute; left: 16px; display: flex; align-items: center; gap: 6px; font-size: 10.5px; color: var(--grey); }
  .contact-row.r1 { top: 140px; }
  .contact-row.r2 { top: 162px; }
  .contact-row .gap { width: 10px; }
  .icon { width: 15px; height: 15px; flex: none; }

  .card-back .brand { left: 0; right: 0; top: 70px; text-align: center; color: var(--paper); font-size: 24px; }
  .card-back .web { position: absolute; left: 0; right: 0; top: 135px; text-align: center; color: var(--paper); font-size: 11.5px; font-weight: 600; }

  /* Letterhead */
  .sheet-backer { position: absolute; left: 502px; top: 160px; width: 492px; height: 700px; background: var(--teal); }
  .letterhead { position: absolute; left: 583px; top: 80px; width: 494px; height: 698px; background: var(--paper); }
  .letterhead .brand { left: 42px; top: 60px; font-size: 18px; display: flex; align-items: center; gap: 7px; }
  .letter-contacts { position: absolute; left: 362px; top: 45px; font-size: 6.4px; color: var(--grey); }
  .letter-contacts li { list-style: none; display: flex; align-items: flex-start; gap: 6px; margin-bottom: 6px; line-height: 1.25; }
  .letter-contacts .icon { width: 11px; height: 11px; }
  .letter-body { position: absolute; left: 39px; top: 200px; width: 418px; font-family: "Arimo", sans-serif; font-size: 6.9px; line-height: 11.9px; color: var(--ink); }
  .letter-body p { margin-bottom: 12px; }
  .signoff-rule { position: absolute; left: 39px; top: 630px; width: 41px; height: 2px; background: var(--teal); }
  .signoff { position: absolute; left: 39px; top: 644px; font-size: 6.5px; line-height: 10.4px; color: var(--ink); }
  .letterhead .cloud-decor { left: 300px; top: 620px; width: 158px; height: 52px; }
</style>
</head>
<body>

  <section class="card card-front">
    <div class="brand"><span class="brand-square"></span>Nestling Rooms</div>
    <div class="cloud-decor" role="img" aria-label="faint cloud decoration"></div>
    <div class="holder-name">Marlo Fenwick</div>
    <div class="holder-role">Business Manager</div>
    <div class="contact-row r1">
      <svg class="icon" viewBox="0 0 16 16"><circle cx="8" cy="8" r="8" fill="var(--teal)"/><path d="M5.3 4.5l1.5-.3.8 2-1 .7a5 5 0 0 0 2.5 2.5l.7-1 2 .8-.3 1.5c-3.4.4-6.6-2.8-6.2-6.2z" fill="#fff"/></svg>
      <span>555 014 2286</span><span class="gap"></span>
      <svg class="icon" viewBox="0 0 16 16"><circle cx="8" cy="8" r="8" fill="var(--teal)"/><rect x="4" y="5.2" width="8" height="5.6" rx=".6" fill="#fff"/><path d="M4.3 5.6L8 8.4l3.7-2.8" stroke="var(--teal)" stroke-width=".9" fill="none"/></svg>
      <span>marlo@nestlingrooms.com</span>
    </div>
    <div class="contact-row r2">
      <svg class="icon" viewBox="0 0 16 16"><circle cx="8" cy="8" r="8" fill="var(--teal)"/><path d="M8 3.6a3 3 0 0 0-3 3c0 2.2 3 5.8 3 5.8s3-3.6 3-5.8a3 3 0 0 0-3-3z" fill="#fff"/><circle cx="8" cy="6.6" r="1.1" fill="var(--teal)"/></svg>
      <span>Street, City State XXXXX Country</span>
    </div>
  </section>

  <section class="card card-back">
    <div class="brand">Nestling Rooms</div>
    <div class="web">www.nestlingrooms.com</div>
  </section>

  <div class="sheet-backer"></div>
  <section class="letterhead">
    <div class="brand"><span class="brand-square"></span>Nestling Rooms</div>
    <ul class="letter-contacts">
      <li><svg class="icon" viewBox="0 0 16 16"><circle cx="8" cy="8" r="8" fill="var(--orange)"/><path d="M8 3.6a3 3 0 0 0-3 3c0 2.2 3 5.8 3 5.8s3-3.6 3-5.8a3 3 0 0 0-3-3z" fill="#fff"/></svg><span>Office #, Building Street, City<br>State XXXXX Country</span></li>
      <li><svg class="icon" viewBox="0 0 16 16"><circle cx="8" cy="8" r="8" fill="var(--orange)"/><path d="M5.3 4.5l1.5-.3.8 2-1 .7a5 5 0 0 0 2.5 2.5l.7-1 2 .8-.3 1.5c-3.4.4-6.6-2.8-6.2-6.2z" fill="#fff"/></svg><span>555 014 2286</span></li>
      <li><svg class="icon" viewBox="0 0 16 16"><circle cx="8" cy="8" r="8" fill="var(--orange)"/><rect x="4" y="5.2" width="8" height="5.6" rx=".6" fill="#fff"/></svg><span>sayhello@nestlingrooms.com</span></li>
      <li><svg class="icon" viewBox="0 0 16 16"><circle cx="8" cy="8" r="8" fill="var(--orange)"/><circle cx="8" cy="8" r="3.4" fill="none" stroke="#fff" stroke-width="1.2"/></svg><span>www.nestlingrooms.com</span></li>
    </ul>
    <div class="letter-body">
      <p>Lorem ipsum dolor sit amet, consectetur adipisicing elit, sed do eiusmod tempor incididunt ut labore et dolore magna aliqua. Ut enim ad minim veniam, quis nostrud exercitation ullamco laboris nisi ut aliquip ex ea commodo consequat. Duis aute irure dolor in reprehenderit in voluptate velit esse cillum dolore eu fugiat nulla pariatur. Excepteur sint occaecat cupidatat non proident, sunt in culpa qui officia deserunt mollit anim id est laborum. Lorem ipsum dolor sit amet, consectetur adipisicing elit, sed do eiusmod tempor incididunt ut labore et dolore magna aliqua. Ut enim ad minim veniam, quis nostrud exercitation ullamco laboris nisi ut aliquip ex ea commodo consequat. Duis aute irure dolor in reprehenderit in voluptate velit esse cillum dolore eu fugiat nulla pariatur. Excepteur sint occaecat cupidatat non proident, sunt in culpa qui officia deserunt mollit anim id est laborum.</p>
      <p>Lorem ipsum dolor sit amet, consectetur adipisicing elit, sed do eiusmod tempor incididunt ut labore et dolore magna aliqua. Ut enim ad minim veniam, quis nostrud exercitation ullamco laboris nisi ut aliquip ex ea commodo consequat. Duis aute irure dolor in reprehenderit in voluptate velit esse cillum dolore eu fugiat nulla pariatur. Excepteur sint occaecat cupidatat non proident, sunt in culpa qui officia deserunt mollit anim id est laborum.</p>
      <p>Lorem ipsum dolor sit amet, consectetur adipisicing elit, sed do eiusmod tempor incididunt ut labore et dolore magna aliqua. Ut enim ad minim veniam, quis nostrud exercitation ullamco laboris nisi ut aliquip ex ea commodo consequat. Duis aute irure dolor in reprehenderit in voluptate velit esse cillum dolore eu fugiat nulla pariatur. Excepteur sint occaecat cupidatat non proident, sunt in culpa qui officia deserunt mollit anim id est laborum.</p>
    </div>
    <div class="signoff-rule"></div>
    <div class="signoff">Date<br>Initials<br>Designation</div>
    <div class="cloud-decor" role="img" aria-label="faint cloud decoration"></div>
  </section>

</body>
</html>
```